Business card design for Plumbing and Gas fitting company

We need a business card design for our plumbing and gas fitting company using the company logo and director details. Design should be modern and eye-catching however kept reasonably simple. This design should be targeted at commercial businesses/work so professionalism is key.

Target Market(s)

Commercial/business

Industry/Entity Type

Plumbing

Contact Information for Business Card

Warren Dohey
Director
027 581 9043
warren@vantorplumbingandgas.example
PO Box 7816
Palmerston North 4472

Font styles to use
Sans Serif

Requirements
Must have
• Logo
• Modern
• Kept simple
Nice to have
• Colour scheme based around logo

```html
<!DOCTYPE html>
<html lang="en">
<head>
<meta charset="utf-8">
<title>Vantor Plumbing &amp; Gas – Business Card</title>
<link rel="stylesheet" href="https://fonts.googleapis.com/css2?family=Open+Sans:wght@400;600;700&display=swap">
<style>
  :root {
    --bg: #e9e7e4;
    --card-front: #ffffff;
    --card-back: #222222;
    --brand-blue: #1474bb;
    --brand-orange: #ea7a2c;
    --text-grey: #555555;
    --text-soft: #6a6a6a;
  }
  * { box-sizing: border-box; margin: 0; padding: 0; }
  html, body {
    width: 1200px; height: 1000px; overflow: hidden;
    background: var(--bg);
    font-family: "Open Sans", Arial, sans-serif;
  }
  .stage { position: relative; width: 1200px; height: 1000px; }
  .card {
    position: absolute; left: 310px; width: 580px; height: 330px;
    border-radius: 22px;
    box-shadow: 0 6px 18px rgba(0,0,0,0.18);
  }
  .card--front { top: 110px; background: var(--card-front); }
  .card--back { top: 560px; background: var(--card-back); }

  .brand {
    position: absolute; top: 38px; right: 40px;
    display: flex; align-items: center; gap: 10px;
    font-weight: 700; font-size: 19px; color: var(--brand-blue);
  }
  .brand__dot { width: 22px; height: 22px; border-radius: 50%; background: var(--brand-orange); }

  .person { position: absolute; left: 44px; top: 168px; }
  .person__name { font-weight: 700; font-size: 24px; letter-spacing: 0.5px; line-height: 1; }
  .person__first { color: var(--brand-blue); }
  .person__last { color: var(--brand-orange); }
  .person__role { font-size: 20px; color: var(--text-grey); margin-top: 6px; }

  .contacts { position: absolute; left: 44px; top: 238px; list-style: none; }
  .contacts li {
    display: flex; align-items: center; gap: 10px;
    font-size: 14px; color: var(--text-soft); line-height: 21px;
  }
  .contacts svg { width: 15px; height: 15px; fill: var(--brand-orange); flex: none; }

  .back-brand {
    position: absolute; inset: 0;
    display: flex; align-items: center; justify-content: center; gap: 10px;
    font-weight: 700; font-size: 19px; color: var(--brand-orange);
  }
  .back-brand__dot { width: 22px; height: 22px; border-radius: 50%; background: var(--brand-blue); }
</style>
</head>
<body>
<main class="stage">
  <section class="card card--front" aria-label="Business card front">
    <div class="brand">
      <span class="brand__dot"></span>
      <span class="brand__name">Vantor Plumbing &amp; Gas</span>
    </div>

    <div class="person">
      <p class="person__name"><span class="person__first">WARREN</span> <span class="person__last">DOHEY</span></p>
      <p class="person__role">Director</p>
    </div>

    <ul class="contacts">
      <li>
        <svg viewBox="0 0 24 24"><path d="M6.6 10.8a15 15 0 0 0 6.6 6.6l2.2-2.2c.3-.3.7-.4 1-.2 1.1.4 2.3.6 3.6.6.6 0 1 .4 1 1V20c0 .6-.4 1-1 1A17 17 0 0 1 3 4c0-.6.4-1 1-1h3.5c.6 0 1 .4 1 1 0 1.3.2 2.5.6 3.6.1.3 0 .7-.2 1z"/></svg>
        027 581 9043
      </li>
      <li>
        <svg viewBox="0 0 24 24"><path d="M2 5h20v14H2z" opacity=".95"/><path d="M2 5l10 8 10-8" fill="none" stroke="#fff" stroke-width="1.8"/></svg>
        warren@vantorplumbingandgas.example
      </li>
      <li>
        <svg viewBox="0 0 24 24"><circle cx="12" cy="12" r="10"/><path d="M2 12h20M12 2c3 3 3 17 0 20M12 2c-3 3-3 17 0 20M4 7h16M4 17h16" fill="none" stroke="#fff" stroke-width="1.4"/></svg>
        www.vantorplumbingandgas.example
      </li>
      <li>
        <svg viewBox="0 0 24 24"><path d="M12 2a7 7 0 0 0-7 7c0 5 7 13 7 13s7-8 7-13a7 7 0 0 0-7-7zm0 9.5A2.5 2.5 0 1 1 12 6.5a2.5 2.5 0 0 1 0 5z"/></svg>
        PO Box 7816, Palmerston North 4472
      </li>
    </ul>
  </section>

  <section class="card card--back" aria-label="Business card back">
    <div class="back-brand">
      <span class="back-brand__dot"></span>
      <span>Vantor Plumbing &amp; Gas</span>
    </div>
  </section>
</main>
</body>
</html>
```